Business card design needed

I would like a one sided black business card with the information provided above. Refer to my website www.lobcrafttennis.com.au for an example of colors I have used for my site, would like to keep this consistent for my business cards also, I will upload my logo below.

I am a new small business that provides tennis customers with racquet re stringing, tennis strings and accessories.

Industry/Entity Type

Small Business

Contact Information for Business Card

Lob Craft Tennis

Dennis Morrow
Managing Director

lobcrafttennis@mailbay.com
www.lobcrafttennis.com.au
0412 695 203

Racquet Restringing/Tennis Strings/Accessories

Requirements
Must have
• Must have my logo and card must be black

```html
<!DOCTYPE html>
<html lang="en">
<head>
<meta charset="utf-8">
<title>Lob Craft Tennis – Business Card</title>
<link rel="stylesheet" href="https://fonts.googleapis.com/css2?family=Lato:ital,wght@0,400;0,700;1,400&display=swap">
<style>
  :root {
    --page-bg: #2b2b2b;
    --card-black: #0b0b0b;
    --card-glow: #262626;
    --lime: #c9e120;
    --link-blue: #3a6cc2;
    --bullet-blue: #4a8fd8;
    --text-white: #f2f2f2;
    --text-soft: #d9d2c6;
    --ghost: rgba(255,255,255,0.035);
  }
  * { margin: 0; padding: 0; box-sizing: border-box; }
  html, body {
    width: 1200px; height: 949px; overflow: hidden;
    background: var(--page-bg);
    font-family: "Lato", "Gill Sans", sans-serif;
  }
  .business-card {
    position: absolute; left: 150px; top: 222px;
    width: 900px; height: 505px;
    background:
      radial-gradient(ellipse 60% 45% at 72% 22%, var(--card-glow), transparent 70%),
      repeating-linear-gradient(45deg, rgba(255,255,255,0.012) 0 2px, transparent 2px 4px),
      var(--card-black);
    box-shadow: 0 10px 30px rgba(0,0,0,0.6);
    overflow: hidden;
  }
  .ghost-name {
    position: absolute; left: 300px; top: 300px;
    font-size: 92px; font-weight: 700; color: var(--ghost);
    white-space: nowrap; letter-spacing: 2px;
  }
  .service-list {
    position: absolute; left: 88px; top: 94px;
    list-style: none; color: var(--text-white);
    font-size: 27px; line-height: 36.5px;
  }
  .service-list li { display: flex; align-items: center; gap: 16px; }
  .service-list li::before {
    content: ""; width: 14px; height: 14px; border-radius: 50%;
    background: radial-gradient(circle at 35% 35%, #9cc8f2, var(--bullet-blue) 60%, #1f4f8a);
  }
  .brand {
    position: absolute; left: 460px; top: 62px;
    display: flex; align-items: center; gap: 14px;
  }
  .brand-dot { width: 40px; height: 40px; border-radius: 50%; background: var(--lime); }
  .brand-name {
    font-size: 40px; font-weight: 700; color: var(--lime);
    text-transform: uppercase; letter-spacing: 1px; white-space: nowrap;
  }
  .website {
    position: absolute; left: 472px; top: 212px;
    font-size: 22px; color: var(--link-blue);
  }
  .contact { position: absolute; left: 88px; top: 296px; }
  .person-name { font-size: 36px; color: var(--text-white); line-height: 44px; }
  .person-title { font-size: 23px; font-style: italic; color: var(--lime); line-height: 28px; }
  .phone {
    display: flex; align-items: center; gap: 12px;
    margin-top: 10px; font-size: 33px; color: var(--text-white); line-height: 40px;
  }
  .phone svg { width: 38px; height: 38px; }
  .email { font-size: 23px; color: var(--text-soft); margin-top: 4px; }
</style>
</head>
<body>
  <main class="business-card">
    <div class="ghost-name" aria-hidden="true">Lob Craft Tennis</div>

    <ul class="service-list">
      <li>Racquet Restringing</li>
      <li>Tennis Strings</li>
      <li>Accessories</li>
    </ul>

    <div class="brand">
      <span class="brand-dot"></span>
      <span class="brand-name">Lob Craft Tennis</span>
    </div>
    <div class="website">www.lobcrafttennis.com.au</div>

    <section class="contact">
      <p class="person-name">Dennis Morrow</p>
      <p class="person-title">Managing Director</p>
      <p class="phone">0412 695 203
        <svg viewBox="0 0 38 38" aria-hidden="true">
          <circle cx="19" cy="19" r="16.5" fill="none" stroke="#d9d2c6" stroke-width="2"/>
          <path d="M13 11c1-1 2.5-1 3 0l2 3.5c.4.8.2 1.6-.5 2.1l-1.3 1c.8 2 2.3 3.6 4.3 4.4l1-1.3c.5-.7 1.4-.9 2.1-.5l3.5 2c1 .6 1 2 0 3l-1.6 1.6c-1.4 1.4-4 1.2-7.2-.8-3.2-2-5.7-5-7-8.2-1-2.6-.8-4.9.6-6.2z" fill="#d9d2c6"/>
        </svg>
      </p>
      <p class="email">lobcrafttennis@mailbay.com</p>
    </section>
  </main>
</body>
</html>
```